Business Cards for a law firm

Business cards for our law firm. Use our silhoette logo and OAK HARBOR - check our website (www.oakharbor-legal.com)

Contact Information for Business Card

our silhouette logo, OAK HARBOR, 800-555-0147, Dorian Kestrup, dorian@oakharbor-legal.com

Requirements
Must have
• our silhouette logo, OAK HARBOR, 800-555-0147, Dorian Kestrup, dorian@oakharbor-legal.com

```html
<!DOCTYPE html>
<html lang="en">
<head>
<meta charset="utf-8">
<title>Oak Harbor — Business Cards</title>
<link rel="stylesheet" href="https://fonts.googleapis.com/css2?family=Cinzel:wght@700&family=Jost:wght@300;400;500;600;700&display=swap">
<style>
  :root {
    --navy: #1b3169;
    --gold: #f5a623;
    --white: #ffffff;
    --page: #ffffff;
  }
  * { box-sizing: border-box; margin: 0; padding: 0; }
  html, body { width: 1200px; height: 1015px; overflow: hidden; background: var(--page); }
  body { position: relative; font-family: "Jost", sans-serif; }

  .card {
    position: absolute;
    left: 299px;
    width: 630px;
    height: 360px;
    overflow: hidden;
  }
  .card-front { top: 104px; background: var(--white); }
  .card-back  { top: 536px; background: var(--navy); color: var(--white); }

  /* Front */
  .brand-name {
    position: absolute;
    top: 118px;
    left: 0; right: 0;
    text-align: center;
    font-family: "Cinzel", serif;
    font-weight: 700;
    font-size: 44px;
    letter-spacing: 3px;
    color: var(--navy);
    line-height: 1;
  }
  .tagline-band {
    position: absolute;
    top: 232px; left: 0;
    width: 100%; height: 77px;
    background: var(--navy);
    color: var(--white);
    text-align: center;
  }
  .tagline-headline {
    margin-top: 13px;
    font-weight: 600;
    font-size: 25px;
    letter-spacing: 2px;
    line-height: 1.1;
  }
  .tagline-sub {
    margin-top: 3px;
    font-weight: 400;
    font-size: 14.5px;
    letter-spacing: 1.2px;
  }
  .website {
    position: absolute;
    top: 322px; left: 0; right: 0;
    text-align: center;
    font-weight: 700;
    font-size: 14px;
    letter-spacing: 7px;
    color: var(--navy);
  }

  /* Back */
  .contact-block { position: absolute; left: 0; right: 0; text-align: center; }
  .icon { display: block; margin: 0 auto; }
  .icon-person { position: absolute; top: 48px; left: 302px; }
  .person-name {
    top: 88px;
    font-weight: 600;
    font-size: 25px;
    letter-spacing: 5px;
  }
  .icon-phone { position: absolute; top: 133px; left: 305px; }
  .label {
    font-weight: 700;
    font-size: 11px;
    letter-spacing: 6px;
    color: var(--gold);
  }
  .label-phone { top: 163px; }
  .phone {
    top: 182px;
    font-weight: 500;
    font-size: 28px;
    letter-spacing: 4px;
  }
  .icon-mail { position: absolute; top: 234px; left: 305px; }
  .label-mail { top: 262px; }
  .email {
    top: 279px;
    font-weight: 300;
    font-size: 25px;
    letter-spacing: 4px;
  }
</style>
</head>
<body>

  <section class="card card-front">
    <div class="brand-name">OAK HARBOR</div>
    <div class="tagline-band">
      <p class="tagline-headline">INJURED? CALL OAK HARBOR!</p>
      <p class="tagline-sub">Over $400,000,000 Recovered For Our Clients</p>
    </div>
    <div class="website">WWW.OAKHARBOR-LEGAL.COM</div>
  </section>

  <section class="card card-back">
    <svg class="icon icon-person" width="26" height="32" viewBox="0 0 26 32" fill="none" stroke="#ffffff" stroke-width="1.2" aria-hidden="true">
      <circle cx="13" cy="9" r="6.5"/>
      <path d="M1.5 31 V24 Q1.5 18 8 17.5 L13 22 L18 17.5 Q24.5 18 24.5 24 V31 Z"/>
    </svg>
    <p class="contact-block person-name">DORIAN KESTRUP</p>

    <svg class="icon icon-phone" width="22" height="22" viewBox="0 0 24 24" fill="none" stroke="#ffffff" stroke-width="1.2" aria-hidden="true">
      <path d="M5 2.5 L8.5 2.5 L10 7 L7.8 8.8 Q9.5 13 14.5 16 L16.5 13.8 L21 15.3 L21 19 Q20.5 21.5 17.5 21.2 Q9 20 3.5 11 Q2 7 2.5 4.5 Q3 2.5 5 2.5 Z"/>
    </svg>
    <p class="contact-block label label-phone">CONTACT US FOR A FREE</p>
    <p class="contact-block phone">(800) 555 0147</p>

    <svg class="icon icon-mail" width="20" height="15" viewBox="0 0 20 15" fill="none" stroke="#ffffff" stroke-width="1.2" aria-hidden="true">
      <rect x="0.6" y="0.6" width="18.8" height="13.8"/>
      <path d="M0.6 0.6 L10 8.5 L19.4 0.6 M0.6 14.4 L7.5 6.5 M19.4 14.4 L12.5 6.5"/>
    </svg>
    <p class="contact-block label label-mail">WE’LL GET BACK TO YOU</p>
    <p class="contact-block email">dorian@oakharbor-legal.com</p>
  </section>

</body>
</html>
```